Business card design needed

I need a business card for my new Food & Lifestyle Coaching business - "Bloomwell Food & Lifestlye Coaching"

i already have a logo and would like to have that incorporated into the business card, obviously.

i would like a design that says "fresh" and "funky" - my target market is female, aged 20-45 so i want something that will stand out to them when they see it.

My "Company Colour" is Apple Green
Updates

Thankyou to everyone who has submitted a design for my project. At this stage i have quite a large number of designs to chose from and with only a short time until my project closes i am focusing now on chosing from those i have already shortlisted so am unfortunately not considering any new desings.

Thankyou again for your interest in my project.

Target Market(s)

Female, Health Conscious (or looking to improve their health/lifestyle), aged between 20-45

Industry/Entity Type

Business

Contact Information for Business Card

Tessa Harlow
Ph: 0438215790
Email: hellobloom@quarlmail.com

Requirements
Must have
• Must include my existing Logo
Nice to have
• Would be nice to incoirporate and appointment card on the back

```html
<!DOCTYPE html>
<html lang="en">
<head>
<meta charset="utf-8">
<title>Bloomwell Food &amp; Lifestlye Coaching — Business Card</title>
<link rel="stylesheet" href="https://fonts.googleapis.com/css2?family=Comfortaa:wght@400;600&family=Lora:wght@700&family=Open+Sans:wght@400&display=swap">
<style>
  :root {
    --page: #e6e8e3;
    --card-dark: #27331a;
    --card-mid: #3b4c27;
    --card-sheen: #4c5f33;
    --apple: #8cc63f;
    --apple-soft: #b5dc78;
    --edge: #141a0d;
    --ink-light: #f4f6ef;
    --dots: #a8c98a;
  }
  * { box-sizing: border-box; margin: 0; padding: 0; }
  html, body { width: 1200px; height: 900px; overflow: hidden; }
  body {
    background: var(--page);
    display: flex;
    flex-direction: column;
    align-items: center;
    justify-content: center;
    gap: 44px;
  }
  .card {
    position: relative;
    width: 700px;
    height: 400px;
    border-radius: 4px;
    overflow: hidden;
    background: linear-gradient(160deg, var(--card-mid) 0%, var(--card-dark) 100%);
    box-shadow: 0 10px 28px rgba(0,0,0,.28);
  }
  .card__art { position: absolute; inset: 0; width: 100%; height: 100%; }

  /* front */
  .brand {
    position: absolute;
    left: 255px;
    top: 105px;
    display: flex;
    flex-direction: column;
    align-items: flex-end;
  }
  .brand__row { display: flex; align-items: center; gap: 16px; }
  .brand__dot {
    width: 22px; height: 22px; border-radius: 50%;
    background: var(--apple);
  }
  .brand__name {
    font-family: 'Comfortaa', sans-serif;
    font-weight: 600;
    font-size: 76px;
    line-height: 1;
    color: var(--ink-light);
    letter-spacing: 1px;
  }
  .brand__tagline {
    margin-top: 10px;
    font-family: 'Comfortaa', sans-serif;
    font-weight: 400;
    font-size: 19px;
    color: var(--ink-light);
  }

  /* back */
  .contact {
    position: absolute;
    right: 70px;
    top: 120px;
    text-align: left;
  }
  .contact__name {
    font-family: 'Lora', serif;
    font-weight: 700;
    font-size: 46px;
    color: var(--ink-light);
    letter-spacing: .5px;
  }
  .contact__list { list-style: none; margin-top: 12px; }
  .contact__item {
    display: flex; align-items: center; gap: 10px;
    font-family: 'Open Sans', sans-serif;
    font-size: 20px;
    color: var(--apple-soft);
    line-height: 1.55;
  }
  .contact__icon { width: 18px; height: 18px; flex: none; }
</style>
</head>
<body>

  <section class="card card--front" aria-label="Card front">
    <svg class="card__art" viewBox="0 0 700 400" aria-hidden="true">
      <path d="M0 0 H700 V60 C520 40 300 70 0 140 Z" fill="var(--card-sheen)" opacity=".45"/>
      <path d="M250 250 C300 262 330 240 380 252 S480 262 560 238" fill="none" stroke="var(--dots)" stroke-width="2" stroke-dasharray="2 5" stroke-linecap="round"/>
      <path d="M0 352 L700 290 L700 302 L0 364 Z" fill="var(--apple)"/>
      <path d="M0 364 L700 302 L700 306 L0 368 Z" fill="var(--edge)"/>
      <path d="M0 368 L700 306 V400 H0 Z" fill="var(--card-dark)"/>
    </svg>
    <div class="brand">
      <div class="brand__row">
        <span class="brand__dot"></span>
        <span class="brand__name">Bloomwell</span>
      </div>
      <span class="brand__tagline">Food &amp; Lifestlye Coaching</span>
    </div>
  </section>

  <section class="card card--back" aria-label="Card back">
    <svg class="card__art" viewBox="0 0 700 400" aria-hidden="true">
      <path d="M0 0 H700 V30 C520 20 260 60 0 150 Z" fill="var(--card-sheen)" opacity=".45"/>
      <path d="M150 380 C220 300 330 250 700 215" fill="none" stroke="var(--dots)" stroke-width="1.5" stroke-dasharray="2 5" stroke-linecap="round" opacity=".6"/>
      <path d="M0 380 L700 300 L700 314 L0 394 Z" fill="var(--apple)"/>
      <path d="M0 394 L700 314 V400 H0 Z" fill="var(--edge)"/>
    </svg>
    <div class="contact">
      <h1 class="contact__name">Tessa Harlow</h1>
      <ul class="contact__list">
        <li class="contact__item">
          <svg class="contact__icon" viewBox="0 0 24 24" aria-hidden="true"><path d="M6.6 10.8a15 15 0 0 0 6.6 6.6l2.2-2.2a1 1 0 0 1 1-.25 11 11 0 0 0 3.6.6 1 1 0 0 1 1 1V20a1 1 0 0 1-1 1A17 17 0 0 1 3 4a1 1 0 0 1 1-1h3.5a1 1 0 0 1 1 1 11 11 0 0 0 .6 3.6 1 1 0 0 1-.25 1z" fill="var(--ink-light)"/></svg>
          0438 - 215 - 790
        </li>
        <li class="contact__item">
          <svg class="contact__icon" viewBox="0 0 24 24" aria-hidden="true"><rect x="2" y="5" width="20" height="14" rx="1.5" fill="var(--ink-light)"/><path d="M3 6.5l9 6.5 9-6.5" fill="none" stroke="var(--card-dark)" stroke-width="1.6"/></svg>
          hellobloom@quarlmail.com
        </li>
      </ul>
    </div>
  </section>

</body>
</html>
```